Cyber security consulting company need a redesign web site

We need a new stylish and slick web design for our Cyber security company (our old https://vultrimadvisory.com)
Tolvane Consulting is comprised of a dedicated team of security experts who each have a wide range of expertise and experience in all areas of information security and Cyber such as APT (Advanced persistent threat ) test, penetration test, professional services, Standard & regulation Audit (e.g. ISO27001/2 , PCI DSS, WLA) and security assessment

We are looking for single page application (architecture) base on WordPress platform which brings our potential customer overwhelming experience and simple navigation within our new site.

Attached high level design document

Industry/Entity Type

It Company

Coding

Coded - Design and coding required

Font styles to use
Sans Serif

Colors
0255a3
0492cd
3276b5

Requirements
Must have
• The project must include all web element (HTML & CSS, JavaScript etc..) to be install on WordPress without any special requirement (best practices package or add-on package are acceptable)

```html
<!DOCTYPE html>
<html lang="en">
<head>
<meta charset="utf-8">
<title>Tolvane Consulting – Software Security</title>
<link href="https://fonts.googleapis.com/css2?family=Roboto:wght@400;500;700&family=Roboto+Condensed:wght@400&family=Caveat:wght@500&display=swap" rel="stylesheet">
<style>
  :root {
    --brand-deep: #0255a3;
    --brand-bright: #0492cd;
    --brand-mid: #3276b5;
    --hero-dark: #17627a;
    --hero-light: #3aa3b6;
    --button-blue: #2b80d8;
    --white: #ffffff;
    --ink: #1d2530;
    --panel-light: #e8ebef;
    --line-soft: rgba(255,255,255,0.28);
  }
  * { box-sizing: border-box; margin: 0; padding: 0; }
  html, body { width: 1200px; height: 676px; overflow: hidden; }
  body { font-family: "Roboto", Arial, sans-serif; background: var(--white); }

  .site { width: 1200px; height: 676px; display: flex; flex-direction: column; }

  .hero {
    position: relative;
    height: 470px;
    background: linear-gradient(115deg, var(--hero-dark) 0%, #22798f 45%, var(--hero-light) 100%);
    color: var(--white);
  }

  .topbar {
    height: 70px;
    display: flex;
    align-items: center;
    padding: 0 36px;
    border-bottom: 1px solid var(--line-soft);
  }
  .brand { width: 290px; }
  .brand-name { font-size: 28px; font-weight: 700; line-height: 1; color: var(--white); }

  .main-nav { display: flex; gap: 34px; font-size: 15px; font-weight: 500; margin-left: 30px; }
  .main-nav a { color: var(--white); text-decoration: none; }

  .account-actions { margin-left: auto; display: flex; gap: 8px; }
  .btn-login, .btn-quote {
    font-size: 12px; padding: 7px 12px; border-radius: 16px; font-weight: 500;
  }
  .btn-login { border: 1px solid var(--white); color: var(--white); }
  .btn-quote { background: var(--white); color: var(--ink); padding: 7px 14px; }

  .hero-copy { position: absolute; left: 30px; top: 150px; width: 600px; text-align: center; }
  .hero-title {
    font-family: "Caveat", cursive;
    font-weight: 500;
    font-size: 64px;
    text-align: left;
    margin-left: 50px;
    line-height: 1;
  }
  .hero-lead {
    font-family: "Roboto Condensed", "Arial Narrow", sans-serif;
    font-size: 11px;
    line-height: 15px;
    margin-top: 20px;
    white-space: nowrap;
  }
  .hero-buttons { display: flex; justify-content: center; gap: 26px; margin-top: 22px; margin-left: -50px; }
  .hero-btn {
    background: var(--button-blue);
    color: var(--white);
    font-size: 9px;
    font-weight: 500;
    padding: 9px 12px;
    text-transform: uppercase;
    border-radius: 2px;
  }

  .radar-visual {
    position: absolute;
    right: 60px; top: 100px;
    width: 330px; height: 330px;
    border-radius: 50%;
    background: radial-gradient(circle, rgba(255,255,255,0.14) 0%, rgba(255,255,255,0.06) 60%, rgba(255,255,255,0.02) 100%);
  }

  .welcome {
    height: 110px;
    background: linear-gradient(90deg, var(--brand-deep) 0%, var(--brand-mid) 50%, var(--brand-bright) 100%);
    color: var(--white);
    text-align: center;
    padding-top: 12px;
  }
  .welcome-title { font-size: 20px; font-weight: 500; }
  .welcome-rule { border: 0; border-top: 1px dashed rgba(255,255,255,0.7); margin: 12px 60px 14px; }
  .welcome-text { font-size: 12px; line-height: 17px; white-space: nowrap; }

  .services { flex: 1; background: var(--panel-light); text-align: center; padding-top: 18px; }
  .services-title { font-size: 20px; font-weight: 500; color: var(--ink); }
  .services-title .accent { color: var(--brand-bright); }
  .services-rule { border: 0; border-top: 1px dashed var(--brand-bright); margin: 10px 40px 0; }
</style>
</head>
<body>
<div class="site">
  <header class="hero">
    <div class="topbar">
      <div class="brand">
        <span class="brand-name">Tolvane</span>
      </div>
      <nav class="main-nav">
        <a href="#home">HOME</a>
        <a href="#about">ABOUT</a>
        <a href="#services">SERVICES</a>
        <a href="#team">TEAM</a>
        <a href="#contact">CONTACT</a>
      </nav>
      <div class="account-actions">
        <span class="btn-login">Log In</span>
        <span class="btn-quote">Request a Quote</span>
      </div>
    </div>

    <div class="hero-copy">
      <h1 class="hero-title">Software Security</h1>
      <p class="hero-lead">
        Tolvane Consulting has proven time and again that its approach to software security is<br>
        most effective as it is based on the ever-changing world of technology and latest software developments.<br>
        Our all-encompassing approach is catered to the dynamics of your organization, providing you with a gamut of amenities for your app.
      </p>
      <div class="hero-buttons">
        <span class="hero-btn">Our Services</span>
        <span class="hero-btn">Out Team</span>
      </div>
    </div>

    <div class="radar-visual" role="img" aria-label="Faint radar illustration with concentric rings and target points"></div>
  </header>

  <section class="welcome" id="about">
    <h2 class="welcome-title">Welcome to Tolvane Consulting</h2>
    <hr class="welcome-rule">
    <p class="welcome-text">
      Tolvane Consulting is comprised of a dedicated team of security experts who each have a wide range of expertise and experience in all areas of information security. The company was<br>
      founded by Orin Castell and Dael Morrow, and has quickly become a top consulting firm that specializes in Payment Card Industry Standards, including PCI DSS.
    </p>
  </section>

  <section class="services" id="services">
    <h2 class="services-title">Our <span class="accent">Services</span></h2>
    <hr class="services-rule">
  </section>
</div>
</body>
</html>
```